DOUBLE SIDED BROCHURE NEEDED TO PROMOTE DOCTOR

I need a double sided DL size (99mm x 210mm) brochure, promoting a doctor seeing patients in a new area.

I want something professional. I have included the relevant information. I would also like the Dr's picture somwhere in the brochure, with a professional background. I wish to print these tomorrow, so i will pick a winner within 14 hours of posting this ad.

I have included an example of a brochures design that I recently saw, and its definietly a good starting point.

Industry/Entity Type

Medical

```html
<!DOCTYPE html>
<html lang="en">
<head>
<meta charset="utf-8">
<title>Surgeon Referral Brochure – DL Double Sided</title>
<link href="https://fonts.googleapis.com/css2?family=Arimo:wght@400;700&display=swap" rel="stylesheet">
<style>
  :root{
    --bg:#eef0f0;
    --teal:#2a9196;
    --teal-dark:#1f7b80;
    --panel:#d5dbde;
    --ink:#1d3f5e;
    --accent:#2a8a90;
    --line-gold:#e8e2b8;
    --line-white:#e9f1f1;
    --icon:#3fd0e0;
    --icon-deep:#1f8fd6;
  }
  *{box-sizing:border-box;margin:0;padding:0}
  html,body{width:1200px;height:960px;overflow:hidden;background:var(--bg)}
  body{font-family:"Arimo",Arial,sans-serif;position:relative}

  .brochure-side{
    position:absolute;top:56px;width:400px;height:848px;
    background:radial-gradient(ellipse at 50% 45%,var(--teal) 55%,var(--teal-dark) 100%);
    overflow:hidden;box-shadow:0 6px 18px rgba(0,0,0,.18);
  }
  .side-front{left:160px}
  .side-back{left:640px}

  .decor{position:absolute;inset:0;width:100%;height:100%}

  .text-box{
    position:absolute;background:var(--panel);
    box-shadow:inset 0 0 12px rgba(0,0,0,.18);
    color:var(--ink);font-weight:700;
  }

  /* front */
  .letter-box{left:34px;top:26px;width:344px;height:340px;padding:26px 28px;font-size:15.5px;line-height:1.2}
  .letter-box p{margin-bottom:18px}
  .letter-box .indent{text-indent:26px}
  .clinic-box{left:132px;top:418px;width:256px;height:170px;padding:22px 26px;font-size:16px;line-height:1.25}
  .clinic-box .clinic-name{color:var(--accent);margin-bottom:16px}
  .clinic-box .phone-label{color:var(--accent)}
  .clinic-box .address{margin-bottom:14px}
  .referral-note{
    position:absolute;left:26px;top:630px;width:170px;
    color:var(--line-white);font-weight:700;font-size:15px;line-height:1.35;
    white-space:nowrap;
  }
  .portrait{
    position:absolute;right:0;bottom:0;width:186px;height:250px;
    background:linear-gradient(180deg,#8a7c74 0%,#5a4c48 35%,#1d1e24 70%,#15161b 100%);
  }

  /* back */
  .specialty-box{left:20px;top:30px;width:360px;height:404px;padding:30px 30px;font-size:16.5px;line-height:1.25}
  .specialty-box .intro{margin-bottom:18px}
  .bullet-list{list-style:none}
  .bullet-list li{padding-left:14px;position:relative}
  .bullet-list li::before{content:"•";position:absolute;left:0}
  .general-box{left:30px;top:566px;width:352px;height:196px;padding:22px 26px;font-size:16.5px;line-height:1.2}
  .general-box .intro{margin-bottom:6px}
  .medical-emblem{
    position:absolute;left:272px;top:730px;width:104px;height:104px;
    background:linear-gradient(180deg,var(--icon) 0%,var(--icon-deep) 100%);
    border-radius:10px;
  }
</style>
</head>
<body>

<section class="brochure-side side-front">
  <svg class="decor" viewBox="0 0 400 848" aria-hidden="true">
    <rect x="10" y="10" width="380" height="828" fill="none" stroke="var(--line-white)" stroke-width="2" opacity=".7"/>
    <line x1="20" y1="375" x2="20" y2="840" stroke="var(--line-white)" stroke-width="3" opacity=".8"/>
    <line x1="60" y1="400" x2="60" y2="610" stroke="var(--line-gold)" stroke-width="2"/>
    <line x1="60" y1="715" x2="60" y2="820" stroke="var(--line-gold)" stroke-width="2"/>
    <line x1="0" y1="560" x2="130" y2="560" stroke="var(--line-white)" stroke-width="2"/>
    <line x1="0" y1="790" x2="200" y2="790" stroke="var(--line-gold)" stroke-width="2"/>
    <line x1="110" y1="395" x2="390" y2="395" stroke="var(--line-gold)" stroke-width="2"/>
  </svg>
  <div class="text-box letter-box">
    <p>Dear Doctors,</p>
    <p class="indent">We are pleased to announce that Dr. Karim Haddad is now consulting in Coastview, seeing public and private patients.</p>
    <p class="indent">Guaranteed appointment within two weeks, with patients having the option of surgery at Harbourside Health Campus, Riverside General Hospital or St. Clare Southgate.</p>
  </div>
  <div class="text-box clinic-box">
    <p class="clinic-name">Coastview Clinic:</p>
    <p class="address">42 Seabreeze Road<br>Coastview WA 6180.</p>
    <p><span class="phone-label">Phone:</span> 1300 482 917</p>
  </div>
  <p class="referral-note">Please send all<br>referrals by fax to<br>(08) 6200 4418.</p>
  <div class="portrait" role="img" aria-label="Portrait photograph of the surgeon in a dark blazer"></div>
</section>

<section class="brochure-side side-back">
  <svg class="decor" viewBox="0 0 400 848" aria-hidden="true">
    <rect x="10" y="10" width="380" height="828" fill="none" stroke="var(--line-white)" stroke-width="2" opacity=".7"/>
    <line x1="0" y1="470" x2="200" y2="470" stroke="var(--line-white)" stroke-width="3"/>
    <line x1="120" y1="500" x2="340" y2="500" stroke="var(--line-white)" stroke-width="2"/>
    <line x1="200" y1="520" x2="400" y2="520" stroke="var(--line-gold)" stroke-width="2"/>
    <line x1="280" y1="460" x2="280" y2="540" stroke="var(--line-gold)" stroke-width="2"/>
    <line x1="330" y1="490" x2="330" y2="560" stroke="var(--line-gold)" stroke-width="2"/>
    <line x1="20" y1="560" x2="20" y2="840" stroke="var(--line-white)" stroke-width="3" opacity=".8"/>
    <line x1="40" y1="820" x2="260" y2="820" stroke="var(--line-gold)" stroke-width="2"/>
    <line x1="388" y1="30" x2="388" y2="420" stroke="var(--line-gold)" stroke-width="2"/>
  </svg>
  <div class="text-box specialty-box">
    <p class="intro">Dr. Haddad is a highly trained specialised surgeon, in all areas of Endocrine, Breast and General Surgery. Including:</p>
    <ul class="bullet-list">
      <li>Thyroid Surgery</li>
      <li>Parathyroid surgery (including minimally invasive parathyroidectomy)</li>
      <li>Breast Cancer</li>
      <li>Benign breast lesions</li>
    </ul>
  </div>
  <div class="text-box general-box">
    <p class="intro">All areas of general surgery, such as:</p>
    <ul class="bullet-list">
      <li>Gallbladder surgery</li>
      <li>Hernia surgery</li>
      <li>Haemorrhoids</li>
      <li>Carpal Tunnel</li>
      <li>Vasectomy etc etc</li>
    </ul>
  </div>
  <div class="medical-emblem" role="img" aria-label="Medical emblem"></div>
</section>

</body>
</html>
```